Business Card Design Project

I need a business card designed that is clean, simple and elegant.
I am a fashion and advertising photographer based in Cape Town and Durban South Africa.
check out my website: www.marlowvance.co.za for ideas
Updates
Hi all,
Thanks for your submissions so far!
Please note:
I want no more than than black, white and/or grey to be used.
I don't want any photos used.
I would like the card to be double sided.
I would like to continue the design similar to the past ones Ive used.
I hope this helps, please send me further questions should you have any.
many thanks!
Marlow
Hi,
Please have a look at the jpg I loaded(called inspiration) which is the direction or inspiration I am aiming at.
Also PLEASE remember NO PHOTOS to be included on the card
many thanks!!
Target Market(s)
You can look at my site to get a better understanding of the audience:
www.marlowvance.co.za
Industry/Entity Type
Advertising
Requirements
Must have
- Clean design which can also be used for a watermark on photographs
perhaps black background with white text/grey
company called: Marlow Vance Photography
Nice to have
- below I have added logos that I have used in the past.
Should not have
- pictures of cameras
tacky elements

```html
<!DOCTYPE html>
<html lang="en">
<head>
<meta charset="utf-8">
<title>Marlow Vance Photography – Business Card</title>
<link rel="stylesheet" href="https://fonts.googleapis.com/css2?family=Open+Sans:wght@400;600;700&display=swap">
<style>
  :root {
    --backdrop: #b38727;
    --card: #ffffff;
    --card-edge: #3a2a0a;
    --band: #222222;
    --brand-grey: #8a8a8a;
    --ink: #1b1b1b;
  }
  * { box-sizing: border-box; margin: 0; padding: 0; }
  html, body { width: 1200px; height: 686px; overflow: hidden; }
  body {
    position: relative;
    background: var(--backdrop);
    font-family: "Open Sans", Arial, sans-serif;
    color: var(--ink);
  }
  .card {
    position: absolute;
    width: 483px;
    height: 275px;
    background: var(--card);
    border-radius: 30px;
    box-shadow: 1px 2px 0 var(--card-edge);
    overflow: hidden;
  }
  .card--front { left: 86px; top: 157px; }
  .card--back  { left: 621px; top: 283px; height: 276px; }

  .brand-band {
    position: absolute;
    background: var(--band);
    display: flex;
    flex-direction: column;
    justify-content: center;
    align-items: center;
    color: var(--brand-grey);
    font-weight: 600;
    text-transform: uppercase;
    line-height: 1;
  }
  .card--front .brand-band {
    left: 0; top: 81px; width: 250px; height: 120px;
    font-size: 27px; letter-spacing: 1px; gap: 3px;
  }
  .card--front .brand-band .brand-line--small { font-size: 17px; letter-spacing: 2px; margin-top: 4px; }
  .card--back .brand-band {
    left: 171px; top: 78px; width: 312px; height: 120px;
    font-size: 23px; letter-spacing: 1px; gap: 2px;
  }

  .contact {
    position: absolute;
    left: 264px;
    top: 79px;
  }
  .contact__name { font-size: 17px; font-weight: 700; line-height: 1.2; }
  .contact__title { font-size: 12px; font-weight: 600; margin-top: 3px; }
  .contact__list { list-style: none; margin-top: 14px; }
  .contact__item {
    display: flex; align-items: center; gap: 6px;
    font-size: 12.5px; line-height: 18px;
  }
  .contact__item svg { width: 11px; height: 11px; flex: none; fill: var(--ink); }
</style>
</head>
<body>
  <section class="card card--front" aria-label="Card front">
    <div class="brand-band">
      <span class="brand-line">Marlow</span>
      <span class="brand-line">Vance</span>
      <span class="brand-line brand-line--small">Photography</span>
    </div>
    <div class="contact">
      <p class="contact__name">Your Name</p>
      <p class="contact__title">Title</p>
      <ul class="contact__list">
        <li class="contact__item">
          <svg viewBox="0 0 24 24"><path d="M6.6 10.8a15 15 0 0 0 6.6 6.6l2.2-2.2c.3-.3.7-.4 1-.2 1.1.4 2.3.6 3.6.6.6 0 1 .4 1 1V20c0 .6-.4 1-1 1A17 17 0 0 1 3 4c0-.6.4-1 1-1h3.5c.6 0 1 .4 1 1 0 1.3.2 2.5.6 3.6.1.3 0 .7-.2 1z"/></svg>
          123-456-7890
        </li>
        <li class="contact__item">
          <svg viewBox="0 0 24 24"><path d="M6 2h10l2 2v5H6zM3 10h18v9h-3v3H6v-3H3zm5 6v4h8v-4zm-3-4v2h2v-2z"/></svg>
          123-456-7890
        </li>
        <li class="contact__item">
          <svg viewBox="0 0 24 24"><path d="M2 5h20v2l-10 6L2 7zm0 4.5 10 6 10-6V19H2z"/></svg>
          studio@marlowvance.com
        </li>
        <li class="contact__item">
          <svg viewBox="0 0 24 24"><path d="M12 2a10 10 0 1 0 0 20 10 10 0 0 0 0-20zm6.9 6h-3a15 15 0 0 0-1.4-3.9A8 8 0 0 1 18.9 8zM12 4c.8 1.2 1.5 2.5 1.9 4h-3.8c.4-1.5 1.1-2.8 1.9-4zM4.3 14a8 8 0 0 1 0-4h3.4a16 16 0 0 0 0 4zm.8 2h3a15 15 0 0 0 1.4 3.9A8 8 0 0 1 5.1 16zm3-8h-3a8 8 0 0 1 4.4-3.9C8.9 5.3 8.4 6.6 8.1 8zM12 20c-.8-1.2-1.5-2.5-1.9-4h3.8c-.4 1.5-1.1 2.8-1.9 4zm2.3-6H9.7a14 14 0 0 1 0-4h4.6a14 14 0 0 1 0 4zm.2 5.9c.6-1.2 1.1-2.5 1.4-3.9h3a8 8 0 0 1-4.4 3.9zm1.8-5.9a16 16 0 0 0 0-4h3.4a8 8 0 0 1 0 4z"/></svg>
          www.marlowvance.co.za
        </li>
      </ul>
    </div>
  </section>

  <section class="card card--back" aria-label="Card back">
    <div class="brand-band">
      <span class="brand-line">Marlow Vance</span>
      <span class="brand-line">Photography</span>
    </div>
  </section>
</body>
</html>
```